Client Voice Framework

We're a not-for profit home health care company. We're creating a new way of doing business that relies on the insights, ideas and "voice" of our clients as part of our planning, training and evaluation.

We need to promote this idea within our company to our workers and also to show the outside world what we're doing with a "framework." We've simplified the ideas to a "star image" (see attached). I like the idea of the five components (i.e. communication, leadership, support, evaluation, client centred culture) surrounding the result or "centre" of improvements. It could be a more attractive version of the star OR something completely different that captures this idea. The design could incorporate images of clients and family members as well and I've attached a few.

Target Market(s)

Our internal staff and clients--showing diversity is very important.

Industry/Entity Type

Home Health Care

Requirements
Must have
• 1 page with the text included in the "Star Drawing" attachment.
• Title: Integrating the Client Voice at RKN
• Our logo
Nice to have
• Images of clients somewhere.
• Could have the idea of the "client voice" somewhere in it.

```html
<!DOCTYPE html>
<html lang="en">
<head>
<meta charset="utf-8">
<title>Client Voice Framework – RKN</title>
<link rel="stylesheet" href="https://fonts.googleapis.com/css2?family=Source+Sans+3:wght@400;600;700&family=Crimson+Text&display=swap">
<style>
  :root {
    --navy: #14197a;
    --pink: #e0106f;
    --white: #ffffff;
    --arrow: #b9c2e6;
  }
  html, body {
    margin: 0;
    padding: 0;
    overflow: hidden;
    background: var(--white);
  }
  .canvas {
    position: relative;
    width: 1200px;
    height: 900px;
    overflow: hidden;
    font-family: "Source Sans 3", "Myriad Pro", sans-serif;
    color: var(--navy);
  }
  .framework-art {
    position: absolute;
    inset: 0;
  }
  .component {
    position: absolute;
    width: 180px;
    text-align: center;
    transform: translate(-50%, -50%);
  }
  .component-title {
    margin: 0;
    font-weight: 700;
    font-size: 21px;
    line-height: 1.15;
    letter-spacing: 0.2px;
  }
  .component-detail {
    margin: 6px 0 0;
    font-size: 15.5px;
    line-height: 1.4;
  }
  .leadership { left: 605px; top: 145px; }
  .communication { left: 848px; top: 360px; }
  .support { left: 355px; top: 345px; width: 185px; }
  .support .component-detail { font-size: 15px; line-height: 1.42; }
  .evaluation { left: 435px; top: 650px; }
  .culture { left: 770px; top: 650px; }

  .outcomes {
    position: absolute;
    left: 600px;
    top: 348px;
    transform: translateX(-50%);
    text-align: center;
    color: var(--white);
  }
  .outcomes-heading {
    margin: 0 0 10px;
    font-size: 26px;
    font-weight: 700;
    letter-spacing: 0.5px;
  }
  .outcomes-list {
    list-style: none;
    margin: 0;
    padding: 0;
    font-size: 20px;
    line-height: 33px;
    white-space: nowrap;
  }
  .brand {
    position: absolute;
    left: 600px;
    top: 738px;
    transform: translateX(-50%);
    text-align: center;
    color: var(--white);
    white-space: nowrap;
  }
  .brand-name {
    margin: 0;
    font-size: 24px;
    font-weight: 700;
    letter-spacing: 0.3px;
  }
  .brand-tagline {
    margin: 6px 0 0;
    font-family: "Crimson Text", Georgia, serif;
    font-size: 18px;
  }
</style>
</head>
<body>
<main class="canvas">
  <svg class="framework-art" width="1200" height="900" viewBox="0 0 1200 900">
    <defs>
      <radialGradient id="photo-warm" cx="50%" cy="50%" r="50%">
        <stop offset="0%" stop-color="#b58e74"/>
        <stop offset="80%" stop-color="#d9c6b4"/>
        <stop offset="100%" stop-color="#ffffff"/>
      </radialGradient>
      <radialGradient id="photo-cool" cx="50%" cy="50%" r="50%">
        <stop offset="0%" stop-color="#9aa3a8"/>
        <stop offset="80%" stop-color="#dcdfe0"/>
        <stop offset="100%" stop-color="#ffffff"/>
      </radialGradient>
      <radialGradient id="photo-sage" cx="50%" cy="50%" r="50%">
        <stop offset="0%" stop-color="#a09a7e"/>
        <stop offset="80%" stop-color="#dcd8c8"/>
        <stop offset="100%" stop-color="#ffffff"/>
      </radialGradient>
    </defs>

    <g class="client-photos">
      <circle role="img" aria-label="Photo of a smiling caregiver embracing an older client in a cap" cx="410" cy="200" r="200" fill="url(#photo-warm)"/>
      <circle role="img" aria-label="Photo of a care worker chatting with an older woman in a striped sweater" cx="800" cy="200" r="190" fill="url(#photo-cool)"/>
      <circle role="img" aria-label="Photo of an older couple hugging and laughing" cx="320" cy="560" r="180" fill="url(#photo-warm)"/>
      <circle role="img" aria-label="Photo of a smiling older man in glasses seated at home" cx="890" cy="560" r="180" fill="url(#photo-sage)"/>
    </g>

    <path class="star-core"
          d="M565 230 Q520 300 445 325 Q470 440 470 560 L423 740 A185 185 0 1 0 777 740 L730 560 Q735 440 770 325 Q690 300 645 230 Z"
          fill="var(--navy)" stroke="var(--pink)" stroke-width="2"/>

    <g class="direction-arrows" fill="var(--arrow)">
      <polygon points="572,262 638,262 605,284"/>
      <polygon points="760,340 760,392 737,366"/>
      <polygon points="452,340 452,392 474,366"/>
      <polygon points="482,560 520,560 508,590"/>
      <polygon points="722,560 684,560 696,590"/>
    </g>

    <g class="component-circles" fill="var(--white)" stroke="var(--pink)" stroke-width="2">
      <circle cx="605" cy="150" r="95"/>
      <circle cx="848" cy="352" r="95"/>
      <circle cx="355" cy="348" r="95"/>
      <circle cx="435" cy="650" r="95"/>
      <circle cx="770" cy="650" r="95"/>
    </g>
  </svg>

  <section class="component leadership">
    <h2 class="component-title">LEADERSHIP</h2>
    <p class="component-detail">Strategic alignment,<br>key focus,<br>sponsorship</p>
  </section>
  <section class="component communication">
    <h2 class="component-title">COMMUNICATION</h2>
    <p class="component-detail">Sharing progress,<br>successes,<br>learning</p>
  </section>
  <section class="component support">
    <h2 class="component-title">ONGOING<br>SUPPORT</h2>
    <p class="component-detail">Steering Committee,<br>Best Practices, Tool Kit<br>and other<br>resources</p>
  </section>
  <section class="component evaluation">
    <h2 class="component-title">ONGOING<br>EVALUATION</h2>
  </section>
  <section class="component culture">
    <h2 class="component-title">CLIENT-CENTRED<br>CULTURE</h2>
  </section>

  <section class="outcomes">
    <h1 class="outcomes-heading">IMPROVED</h1>
    <ul class="outcomes-list">
      <li>Quality of Service</li>
      <li>Client Experience</li>
      <li>Client Centred Care</li>
      <li>Job Satisfaction</li>
    </ul>
  </section>

  <footer class="brand">
    <p class="brand-name">RKN Home Care</p>
    <p class="brand-tagline">Caring Close to Home</p>
  </footer>
</main>
</body>
</html>
```